Label Design for American Pet Health Startup

We need your help in creating a line-up of labels for our upcoming products. The products will come in two different sizes/shapes. We have a logo (sourced form GraphiHive!) to start from and a pretty extensive brief (see attached.) The winning design will be bold, simple, and create a strongly branded look to the whole line while allowing consumers to easily sort through the different SKUs.

The logo and other existing design elements are in the attached powerpoint. I will also post some of the source files.

If you choose to compete for this project, please read the creative brief and the powerpoint very carefully before starting.

Thank you for your time and consideration.

Target Market(s)

Pet owners (dog owners, initially) who care deeply about their pets. Their pets are older and may not be thriving the way they once were. The owners want their pets to have the highest quality of life possible, for as long as is practical. They take their pets frequently to the vet and have great faith in veterinary medicine, but they also believe that dietary supplements may have a beneficial effect. They believe this to be possible because they take supplements themselves.

They are probably older--empty nesters or soon to be. They’ve owned their dog for five years or more, or have rescued an older dog from a shelter. Their dog is, in many ways, a full member of their family.

Industry/Entity Type

Pet Care

Font styles to use
Sans Serif

Requirements
Must have
• Please see the attached brief for this detail. I have cut and paste it into this form but it doesn't translate well. Reading the Word document will be easier and the links will work.
• Packaging Creative Considerations: The product packaging needs to . . .
• • Have a strong, branded line look.
• - The logo has already been developed, and I would like you to be guided in your design choices by its structure and color, but I am open to deviations from the existing work if it leads to a strong design
• • Use color or some other design elements to distinguish each SKU from the other
• • Be bold and simple. This product will typically be merchandised online, with very small images of the packaging. Simple and bold design elements will ensure that the products are both noticed and understood.
• - The product will likely be contained within white plastic or aluminum (silver) bottles with white caps/pumps. However, if you believe your design concepts would benefit from a particular color of bottle/container, please illustrate that, as that would be possible to execute.
• • Communicate that these products are for pets without using any clichés. This category is full of packaging with stock photos of dogs and cats. Please avoid this at all costs. Instead, please unleash your creativity to illustrate the products’ nature/purposes.
• A couple of packaging designs I would like you to draw inspiration from:
• o Vemo. This line is for human supplements/vitamins. Notice the strong line look, the simple and bold graphics, and the smart use of color and other design elements to differentiate the SKUs (while still holding it together as a single brand.)
• o Tundo. This line is for pets. Again, notice the strong line look, the smart use of color to differentiate the SKUs, and the simple and bold presentation that translates so well on the screen.
• o Corvalune. This design is not as good as the first two, but it does accomplish several of the brief’s objectives and the packaging is likely to be very similar to what your design will eventually be affixed to.
• Design Deliverables: A great submission will illustrate its strength by showing how the design translates across all the expected SKUs. To accomplish, this, I would recommend using the “functional maps” I’ve included in the attached Powerpoint document to:
• o First illustrate, in greater size and detail, one SKU each of the two families (one oil SKU and one supplement SKU)
• o Then illustrate how each of those designs extends across the rest of the family. That illustration can be less detailed. We just need to see how the colors and other design elements extend.
Should not have
• No stock images of cats or dogs; please avoid junking up the designs with too many elements

```html
<!DOCTYPE html>
<html lang="en">
<head>
<meta charset="utf-8">
<title>Wagwell Soft Chew Supplement Labels</title>
<link href="https://fonts.googleapis.com/css2?family=Bebas+Neue&family=Open+Sans:wght@400;600&display=swap" rel="stylesheet">
<style>
  :root {
    --ink: #000;
    --paper: #fff;
    --brand-teal: #3aa9b8;
    --hip: #3aa9ba; --hip-deep: #2a8d9c; --hip-soft: #a8e0ea;
    --skin: #d3100f; --skin-deep: #a90b0a; --skin-soft: #f59d9d;
    --gut: #c2b00c; --gut-deep: #a69507; --gut-soft: #fff5a8;
    --immune: #5c9220; --immune-deep: #3e7a17; --immune-soft: #b8f25a;
    --multi: #ea520e; --multi-deep: #c9440a; --multi-soft: #ffb47c;
    --flag-red: #c8102e; --flag-blue: #2a3a8c;
  }
  * { box-sizing: border-box; margin: 0; padding: 0; }
  html, body { width: 1200px; height: 856px; overflow: hidden; background: var(--paper); }
  body { position: relative; font-family: "Open Sans", Arial, sans-serif; }

  .label { position: absolute; width: 368px; height: 331px; overflow: hidden; color: var(--paper); background: var(--sku); }
  .label--hip { left: 221px; top: 82px; --sku: var(--hip); --sku-deep: var(--hip-deep); --sku-soft: var(--hip-soft); }
  .label--skin { left: 610px; top: 83px; --sku: var(--skin); --sku-deep: var(--skin-deep); --sku-soft: var(--skin-soft); }
  .label--gut { left: 26px; top: 443px; --sku: var(--gut); --sku-deep: var(--gut-deep); --sku-soft: var(--gut-soft); }
  .label--immune { left: 415px; top: 443px; --sku: var(--immune); --sku-deep: var(--immune-deep); --sku-soft: var(--immune-soft); }
  .label--multi { left: 806px; top: 443px; --sku: var(--multi); --sku-deep: var(--multi-deep); --sku-soft: var(--multi-soft); }

  .brand-bar { position: absolute; left: 0; top: 0; width: 100%; height: 108px; background: var(--ink); text-align: center; }
  .brand-mark { position: absolute; left: 160px; top: 14px; width: 48px; height: 48px; border-radius: 3px; background: var(--brand-teal); }
  .brand-name { position: absolute; left: 0; right: 0; top: 66px; font-size: 29px; font-weight: 400; letter-spacing: 1px; color: var(--paper); line-height: 1; }

  .backdrop { position: absolute; left: 0; top: 108px; width: 368px; height: 223px; }
  .backdrop circle.deep { fill: var(--sku-deep); }
  .backdrop circle.base { fill: var(--sku); }

  .content { position: absolute; left: 0; top: 108px; width: 100%; height: 223px; text-align: center; }
  .product-name { position: absolute; left: 0; right: 0; top: 8px; font-family: "Bebas Neue", "Arial Narrow", sans-serif; font-size: 60px; line-height: 1; letter-spacing: 3px; }
  .product-kicker { position: absolute; left: 0; right: 0; top: 2px; font-family: "Bebas Neue", "Arial Narrow", sans-serif; font-size: 24px; letter-spacing: 2px; line-height: 1; }
  .label--multi .product-name { top: 24px; font-size: 56px; }
  .benefit { position: absolute; left: 20px; right: 20px; top: 74px; font-size: 9px; font-weight: 600; line-height: 14px; color: var(--sku-soft); opacity: .9; }
  .label--multi .benefit { top: 77px; line-height: 12.5px; }
  .format-pill { position: absolute; left: 43px; width: 282px; top: 100px; height: 33px; border-radius: 17px; background: var(--ink); font-size: 16.5px; line-height: 33px; }
  .audience { position: absolute; left: 0; right: 0; top: 135px; font-size: 18px; font-weight: 600; color: var(--sku-soft); }
  .origin { position: absolute; left: 16px; top: 170px; width: 60px; text-align: center; font-size: 9.5px; }
  .origin svg { display: block; margin: 0 auto 6px; }
  .count { position: absolute; left: 164px; top: 162px; width: 40px; height: 40px; border-radius: 50%; background: var(--ink); line-height: 1; }
  .count b { display: block; font-weight: 400; font-size: 15px; margin-top: 7px; }
  .count small { display: block; font-size: 8px; margin-top: 1px; }
  .net-weight { position: absolute; left: 0; right: 0; top: 206px; font-size: 9.5px; }
  .free-from { position: absolute; left: 288px; top: 170px; list-style: none; text-align: left; font-size: 11.5px; line-height: 14.5px; }
  .free-from li::before { content: ""; display: inline-block; width: 8px; height: 8px; margin-right: 4px; border-radius: 50%; background: var(--paper); vertical-align: 0; }
</style>
</head>
<body>

<svg width="0" height="0" style="position:absolute">
  <defs>
    <symbol id="us-flag" viewBox="0 0 44 26">
      <rect width="44" height="26" fill="#fff"/>
      <g fill="#c8102e">
        <rect y="0" width="44" height="2"/><rect y="4" width="44" height="2"/><rect y="8" width="44" height="2"/>
        <rect y="12" width="44" height="2"/><rect y="16" width="44" height="2"/><rect y="20" width="44" height="2"/><rect y="24" width="44" height="2"/>
      </g>
      <rect width="19" height="14" fill="#2a3a8c"/>
    </symbol>
    <symbol id="rings" viewBox="0 0 368 223">
      <circle class="deep" cx="140" cy="110" r="215"/>
      <circle class="base" cx="150" cy="110" r="150" opacity=".35"/>
      <circle class="base" cx="186" cy="2" r="100"/>
    </symbol>
  </defs>
</svg>

<section class="label label--hip">
  <header class="brand-bar"><span class="brand-mark"></span><p class="brand-name">Wagwell</p></header>
  <svg class="backdrop" viewBox="0 0 368 223"><use href="#rings"/></svg>
  <div class="content">
    <h2 class="product-name">Hip &amp; Joint</h2>
    <p class="benefit">Supports Healthy Joints with Glucosamine Chondroitin,<br>&amp; Willow Bark</p>
    <p class="format-pill">Soft &amp; Chewable Supplements</p>
    <p class="audience">For Dogs</p>
    <p class="origin"><svg width="44" height="26"><use href="#us-flag"/></svg>Made in USA</p>
    <p class="count"><b>90</b><small>chews</small></p>
    <p class="net-weight">Net Wt 16 OZ / 453 g</p>
    <ul class="free-from"><li>No Gluten</li><li>No Grain</li><li>No Soy</li></ul>
  </div>
</section>

<section class="label label--skin">
  <header class="brand-bar"><span class="brand-mark"></span><p class="brand-name">Wagwell</p></header>
  <svg class="backdrop" viewBox="0 0 368 223"><use href="#rings"/></svg>
  <div class="content">
    <h2 class="product-name">Skin &amp; Coat</h2>
    <p class="benefit">Supports a Healthy Skin &amp; Coat with B Vitamins<br>Omega-3, &amp; Biotin</p>
    <p class="format-pill">Soft &amp; Chewable Supplements</p>
    <p class="audience">For Dogs</p>
    <p class="origin"><svg width="44" height="26"><use href="#us-flag"/></svg>Made in USA</p>
    <p class="count"><b>90</b><small>chews</small></p>
    <p class="net-weight">Net Wt 16 OZ / 453 g</p>
    <ul class="free-from"><li>No Gluten</li><li>No Grain</li><li>No Soy</li></ul>
  </div>
</section>

<section class="label label--gut">
  <header class="brand-bar"><span class="brand-mark"></span><p class="brand-name">Wagwell</p></header>
  <svg class="backdrop" viewBox="0 0 368 223"><use href="#rings"/></svg>
  <div class="content">
    <h2 class="product-name">Digestion</h2>
    <p class="benefit">Supports Healthy Digestion with Enzymes Pre-Biotics,<br>&amp; Pro-Biotics</p>
    <p class="format-pill">Soft &amp; Chewable Supplements</p>
    <p class="audience">For Dogs</p>
    <p class="origin"><svg width="44" height="26"><use href="#us-flag"/></svg>Made in USA</p>
    <p class="count"><b>90</b><small>chews</small></p>
    <p class="net-weight">Net Wt 16 OZ / 453 g</p>
    <ul class="free-from"><li>No Gluten</li><li>No Grain</li><li>No Soy</li></ul>
  </div>
</section>

<section class="label label--immune">
  <header class="brand-bar"><span class="brand-mark"></span><p class="brand-name">Wagwell</p></header>
  <svg class="backdrop" viewBox="0 0 368 223"><use href="#rings"/></svg>
  <div class="content">
    <h2 class="product-name">Immunity</h2>
    <p class="benefit">Supports a Healthy Immune System with Vitamin B12,<br>Vitamin C, &amp; Zinc</p>
    <p class="format-pill">Soft &amp; Chewable Supplements</p>
    <p class="audience">For Dogs</p>
    <p class="origin"><svg width="44" height="26"><use href="#us-flag"/></svg>Made in USA</p>
    <p class="count"><b>90</b><small>chews</small></p>
    <p class="net-weight">Net Wt 16 OZ / 453 g</p>
    <ul class="free-from"><li>No Gluten</li><li>No Grain</li><li>No Soy</li></ul>
  </div>
</section>

<section class="label label--multi">
  <header class="brand-bar"><span class="brand-mark"></span><p class="brand-name">Wagwell</p></header>
  <svg class="backdrop" viewBox="0 0 368 223"><use href="#rings"/></svg>
  <div class="content">
    <p class="product-kicker">Canine</p>
    <h2 class="product-name">Multi</h2>
    <p class="benefit">A Blend of Vitamins, Minerals<br>&amp; Antioxidants for Daily Health Support</p>
    <p class="format-pill">Soft &amp; Chewable Supplements</p>
    <p class="audience">For Dogs</p>
    <p class="origin"><svg width="44" height="26"><use href="#us-flag"/></svg>Made in USA</p>
    <p class="count"><b>90</b><small>chews</small></p>
    <p class="net-weight">Net Wt 16 OZ / 453 g</p>
    <ul class="free-from"><li>No Gluten</li><li>No Grain</li><li>No Soy</li></ul>
  </div>
</section>

</body>
</html>
```